sticker for cleaning products

it is in the bottle. products are bio-cleaner. Toilet Cleaner - yellow Sanitary Cleaner - orange Glass Cleaner - light blue All purpose cleaner - green Hand Soap - cream Detergent - olive Detergent - rose bottles is used VARIO: https://glasvormenhaus.de/katalog/#Vario shape of the sticker is not geometric. It's something like a cloud / leaf / drop / ?? the sticker has an inner space with only the product name and color. the sticker has an outer space. here we want to mark out "powered by QUENSOLI" (our company name, find logo attached)

```html
<!DOCTYPE html>
<html lang="en">
<head>
<meta charset="utf-8">
<title>QUENSOLI Refill – Sticker Set</title>
<link href="https://fonts.googleapis.com/css2?family=Josefin+Sans:wght@600&family=Montserrat:wght@500;600&display=swap" rel="stylesheet">
<style>
  :root {
    --bg: #ffffff;
    --ink: #2a2622;
    --toilet: #f2bd00;          --toilet-in: #f8dc10;
    --sanitary: #e2701a;        --sanitary-in: #efac4c;
    --glass: #5fb6b6;           --glass-in: #a0d8d6;
    --allpurpose: #3a8a32;      --allpurpose-in: #7cbc6c;
    --handsoap: #f0c98c;        --handsoap-in: #f6dfb8;
    --detergent-olive: #8ea228; --detergent-olive-in: #bccb5e;
    --detergent-rose: #e57b6e;  --detergent-rose-in: #f0b0a4;
  }
  * { margin: 0; padding: 0; box-sizing: border-box; }
  html, body { width: 1200px; height: 1200px; overflow: hidden; background: var(--bg); }
  .sheet { position: relative; width: 1200px; height: 1200px; }

  .sticker { position: absolute; width: 172px; height: 292px; }
  .sticker-art {
    position: absolute; inset: 0;
    border-radius: 50% 50% 50% 50% / 62% 62% 38% 38%;
    background: radial-gradient(ellipse at 50% 42%, var(--tone-in) 0%, var(--tone-in) 30%, var(--tone) 75%);
  }
  .sticker-text { position: absolute; left: 0; width: 172px; text-align: center; color: var(--ink); }

  .brand-dot { top: 118px; left: 75px; width: 22px; height: 22px; border: 1.5px solid var(--ink); border-radius: 50%; position: absolute; }
  .brand-name { top: 146px; font-family: "Montserrat", sans-serif; font-weight: 500; font-size: 9px; letter-spacing: 3px; padding-left: 3px; }
  .brand-sub { top: 158px; font-family: "Montserrat", sans-serif; font-weight: 500; font-size: 5px; letter-spacing: 2px; padding-left: 2px; opacity: .6; }
  .product-name { top: 184px; font-family: "Josefin Sans", sans-serif; font-weight: 600; font-size: 23px; line-height: 23px; }
  .product-name--single { top: 196px; }
  .product-name--long { font-size: 20px; line-height: 21px; top: 186px; }
  .volume { top: 256px; font-family: "Montserrat", sans-serif; font-weight: 600; font-size: 9px; }

  .toilet { --tone: var(--toilet); --tone-in: var(--toilet-in); left: 282px; top: 254px; }
  .sanitary { --tone: var(--sanitary); --tone-in: var(--sanitary-in); left: 514px; top: 254px; }
  .glass { --tone: var(--glass); --tone-in: var(--glass-in); left: 746px; top: 252px; }
  .allpurpose { --tone: var(--allpurpose); --tone-in: var(--allpurpose-in); left: 162px; top: 818px; }
  .handsoap { --tone: var(--handsoap); --tone-in: var(--handsoap-in); left: 394px; top: 816px; }
  .detergent-olive { --tone: var(--detergent-olive); --tone-in: var(--detergent-olive-in); left: 622px; top: 818px; }
  .detergent-rose { --tone: var(--detergent-rose); --tone-in: var(--detergent-rose-in); left: 856px; top: 816px; }
</style>
</head>
<body>
<main class="sheet">
  <section class="sticker toilet">
    <div class="sticker-art" role="img" aria-label="Yellow sticker background artwork"></div>
    <span class="brand-dot"></span>
    <div class="sticker-text brand-name">QUENSOLI</div>
    <div class="sticker-text brand-sub">REFILL</div>
    <div class="sticker-text product-name">TOILET<br>CLEANER</div>
    <div class="sticker-text volume">1000 ML</div>
  </section>
  <section class="sticker sanitary">
    <div class="sticker-art" role="img" aria-label="Orange sticker background artwork"></div>
    <span class="brand-dot"></span>
    <div class="sticker-text brand-name">QUENSOLI</div>
    <div class="sticker-text brand-sub">REFILL</div>
    <div class="sticker-text product-name">SANITARY<br>CLEANER</div>
    <div class="sticker-text volume">1000 ML</div>
  </section>
  <section class="sticker glass">
    <div class="sticker-art" role="img" aria-label="Light blue sticker background artwork"></div>
    <span class="brand-dot"></span>
    <div class="sticker-text brand-name">QUENSOLI</div>
    <div class="sticker-text brand-sub">REFILL</div>
    <div class="sticker-text product-name">GLASS<br>CLEANER</div>
    <div class="sticker-text volume">1000 ML</div>
  </section>
  <section class="sticker allpurpose">
    <div class="sticker-art" role="img" aria-label="Green sticker background artwork"></div>
    <span class="brand-dot"></span>
    <div class="sticker-text brand-name">QUENSOLI</div>
    <div class="sticker-text brand-sub">REFILL</div>
    <div class="sticker-text product-name product-name--long">ALL PURPOSE<br>CLEANER</div>
    <div class="sticker-text volume">1000 ML</div>
  </section>
  <section class="sticker handsoap">
    <div class="sticker-art" role="img" aria-label="Cream sticker background artwork"></div>
    <span class="brand-dot"></span>
    <div class="sticker-text brand-name">QUENSOLI</div>
    <div class="sticker-text brand-sub">REFILL</div>
    <div class="sticker-text product-name product-name--single">HAND SOAP</div>
    <div class="sticker-text volume">1000 ML</div>
  </section>
  <section class="sticker detergent-olive">
    <div class="sticker-art" role="img" aria-label="Olive sticker background artwork"></div>
    <span class="brand-dot"></span>
    <div class="sticker-text brand-name">QUENSOLI</div>
    <div class="sticker-text brand-sub">REFILL</div>
    <div class="sticker-text product-name product-name--single">DETERGENT</div>
    <div class="sticker-text volume">1000 ML</div>
  </section>
  <section class="sticker detergent-rose">
    <div class="sticker-art" role="img" aria-label="Rose sticker background artwork"></div>
    <span class="brand-dot"></span>
    <div class="sticker-text brand-name">QUENSOLI</div>
    <div class="sticker-text brand-sub">REFILL</div>
    <div class="sticker-text product-name product-name--single">DETERGENT</div>
    <div class="sticker-text volume">1000 ML</div>
  </section>
</main>
</body>
</html>
```